Health software company called BRIGHT MERIDIAN, committed to innovation and technological excellence

The powerpoint presentation template is necessary, very necessary is elegant and modern with innovative images and the color palette attached. The presentation will be used for the business plan and investor presentations that we will use to raise funds. Please, recommend a modern typeface, as well as format to be able to use it and incorporate it as part of the company's brand guidelines. Great diversity of technological solutions
Updates

Very low attendance of designers for a high budget. Very few proposals and no capture my interest

Need extra days to review

Need extra days to review

Need extra days to review

Target Market(s)

managers, managers of public and private health centers, government states, investors

Industry/Entity Type

It Company

Font styles to use
Serif

Requirements
Must have
• The powerpoint presentation template is necessary, very necessary is elegant, minimalist and modern with innovative images and the color palette attached. it must be refined in demarcated style
Nice to have
• very nice, visually harmonic avoid saturation
Should not have
• NO dark colors NO dark colors NO dark colors NO dark colors NO dark colors

```html
<!DOCTYPE html>
<html lang="en">
<head>
<meta charset="utf-8">
<title>Bright Meridian — Title Slide</title>
<link rel="stylesheet" href="https://fonts.googleapis.com/css2?family=Lora:wght@400&display=swap">
<style>
  :root {
    --deep: #2e6e8c;
    --steel: #4a93ad;
    --teal: #3dbac8;
    --teal-veil: #6ccbd5;
    --mist: #dde2e5;
    --paper: #ffffff;
    --photo-light: #f1f4f6;
    --photo-mid: #d3dde3;
  }
  html, body {
    margin: 0;
    padding: 0;
    width: 1200px;
    height: 900px;
    overflow: hidden;
    background: var(--paper);
  }
  .slide {
    position: relative;
    width: 1200px;
    height: 900px;
    background: var(--paper);
    font-family: "Lora", Georgia, serif;
  }
  .slide__art {
    position: absolute;
    inset: 0;
  }
  .title-block {
    position: absolute;
    right: 778px;
    top: 424px;
    text-align: right;
    color: var(--paper);
  }
  .title-block__name {
    margin: 0;
    font-weight: 400;
    font-size: 38px;
    line-height: 1;
    letter-spacing: 0.5px;
    white-space: nowrap;
  }
  .title-block__tagline {
    margin: 8px 0 0;
    font-weight: 400;
    font-size: 14px;
    line-height: 1.2;
    white-space: nowrap;
  }
  .title-block__bar {
    display: flex;
    justify-content: flex-end;
    margin-top: 14px;
    height: 13px;
  }
  .title-block__bar span { width: 75px; height: 100%; }
  .bar--steel { background: var(--steel); }
  .bar--teal { background: var(--teal); }
  .bar--mist { background: var(--mist); }
</style>
</head>
<body>
<main class="slide">
  <svg class="slide__art" width="1200" height="900" viewBox="0 0 1200 900" xmlns="http://www.w3.org/2000/svg">
    <defs>
      <linearGradient id="photoTone" x1="0" y1="0" x2="1" y2="1">
        <stop offset="0" stop-color="var(--photo-mid)"/>
        <stop offset="0.5" stop-color="var(--photo-light)"/>
        <stop offset="1" stop-color="#e3e9ed"/>
      </linearGradient>
    </defs>

    <polygon class="band-top" fill="var(--deep)"
      points="937.6,78.4 1200,78.4 1200,272 918.4,272 900.8,300.8 800,300.8"/>

    <rect class="title-panel" x="0" y="300.8" width="456.8" height="436" fill="var(--deep)"/>

    <g class="hero">
      <rect role="img" aria-label="Photo: overhead view of a team meeting at a white table with laptops, charts and documents"
        x="467.2" y="300.8" width="732.8" height="436" fill="url(#photoTone)"/>
      <polygon class="hero__veil hero__veil--light" fill="var(--teal-veil)" opacity="0.5"
        points="467.2,300.8 900,300.8 632,736.8 467.2,736.8"/>
      <polygon class="hero__veil hero__veil--deep" fill="var(--teal-veil)" opacity="0.75"
        points="467.2,300.8 800,300.8 560,736.8 467.2,736.8"/>
    </g>

    <g class="stripes">
      <polygon fill="var(--mist)"  points="632,736.8 716,736.8 764,816 680,816"/>
      <polygon fill="var(--teal)"  points="716,736.8 798.4,736.8 846.4,816 764,816"/>
      <polygon fill="var(--steel)" points="798.4,736.8 882.4,736.8 930.4,816 846.4,816"/>
      <polygon fill="var(--deep)"  points="882.4,736.8 1200,736.8 1200,816 930.4,816"/>
    </g>
  </svg>

  <header class="title-block">
    <h1 class="title-block__name">BRIGHT MERIDIAN</h1>
    <p class="title-block__tagline">committed to innovation and technological excellence</p>
    <div class="title-block__bar" aria-hidden="true">
      <span class="bar--steel"></span><span class="bar--teal"></span><span class="bar--mist"></span>
    </div>
  </header>
</main>
</body>
</html>
```